" Somos contratados para prestação de serviços, geralmente em órgãos públicos para nossos clientes. O carro chefe de nossas atuações é Documentação. "

```html
<!DOCTYPE html>
<html lang="pt-BR">
<head>
<meta charset="UTF-8">
<title>Alvora – Pasta Institucional</title>
<link href="https://fonts.googleapis.com/css2?family=Open+Sans:wght@400;600;700;800&display=swap" rel="stylesheet">
<style>
  :root {
    --navy: #1e3554;
    --blue: #2a8fc7;
    --paper: #ffffff;
    --backdrop: #e8e8e6;
    --edge: #cfd3d6;
    --muted: #5a6775;
  }
  * { margin: 0; padding: 0; box-sizing: border-box; }
  html, body { width: 1200px; height: 1200px; overflow: hidden; }
  body {
    background: var(--backdrop);
    font-family: "Open Sans", Arial, sans-serif;
    position: relative;
  }
  .folder-outline { position: absolute; left: 0; top: 0; width: 1200px; height: 1200px; }

  .service-list {
    position: absolute; left: 154px; top: 358px;
    list-style: none; color: var(--navy);
    font-size: 15.5px; font-weight: 700; line-height: 22.5px;
  }
  .service-list li::before {
    content: "›"; color: var(--blue); font-weight: 800; margin-right: 6px;
  }

  .back-footer {
    position: absolute; left: 150px; top: 740px; width: 440px; height: 50px;
    display: flex; align-items: center; gap: 14px; color: var(--navy);
  }
  .brand-small { display: flex; flex-direction: column; }
  .brand-small .brand-name {
    font-size: 19px; font-weight: 700; color: var(--navy);
    display: flex; align-items: center; gap: 6px;
  }
  .brand-small .brand-name::before { content: ""; width: 14px; height: 14px; background: var(--blue); display: inline-block; }
  .brand-small .tagline { font-size: 6.5px; font-weight: 600; letter-spacing: .5px; text-transform: uppercase; color: var(--muted); }
  .footer-divider { width: 1px; height: 36px; background: var(--edge); }
  .contact { display: flex; align-items: center; gap: 6px; font-size: 8px; line-height: 11px; color: var(--muted); }
  .contact svg { flex: none; }
  .contact-address { margin-left: 20px; width: 150px; }

  .front-brand {
    position: absolute; left: 706px; top: 448px; width: 410px;
    display: flex; flex-direction: column; align-items: flex-start;
  }
  .front-brand .brand-name {
    font-size: 52px; font-weight: 700; color: var(--navy); line-height: 1;
    display: flex; align-items: center; gap: 16px;
  }
  .front-brand .brand-name::before { content: ""; width: 40px; height: 40px; background: var(--blue); display: inline-block; }
  .front-brand .tagline {
    margin-left: 58px; margin-top: 8px;
    font-size: 12px; font-weight: 600; letter-spacing: 1.2px; text-transform: uppercase; color: var(--muted);
  }
  .front-rule { position: absolute; left: 628px; top: 767px; width: 488px; height: 6px; background: var(--blue); }
</style>
</head>
<body>
  <svg class="folder-outline" viewBox="0 0 1200 1200" aria-hidden="true">
    <rect x="120" y="108" width="996" height="1020" fill="var(--paper)" stroke="var(--edge)" stroke-width="1.5"/>
    <path d="M120 700 L92 780 L92 1050 L135 1128 L120 1128 Z" fill="var(--paper)" stroke="var(--edge)" stroke-width="1.5"/>
    <path d="M120 800 C260 780 300 900 260 960 C220 1030 330 1100 560 1128" fill="none" stroke="var(--edge)" stroke-width="1.5"/>
    <line x1="619" y1="108" x2="619" y2="1128" stroke="var(--edge)" stroke-width="1.5"/>
  </svg>

  <ul class="service-list">
    <li>Projetos de Engenharia e Arquitetura</li>
    <li>Projetos e Aprovações no Corpo de Bombeiros</li>
    <li>Projetos e processos de aprovação na Aeronáutica</li>
    <li>Anistia e Regularizações de Obras</li>
    <li>Desdobros e Desmembramentos</li>
    <li>Licenças e Alvarás de Funcionamento</li>
    <li>Levantamento Topográfico</li>
    <li>Usucapião</li>
    <li>Inventários</li>
    <li>Laudos</li>
    <li>Projetos de Reformas</li>
    <li>Projetos e Processos em Vigilância Sanitária</li>
    <li>Regularização de Documentação.</li>
    <li>Licença de Publicidade</li>
  </ul>

  <footer class="back-footer">
    <div class="brand-small">
      <span class="brand-name">Alvora</span>
      <span class="tagline">Assessoria e Regularização</span>
    </div>
    <span class="footer-divider"></span>
    <div class="contact">
      <svg width="12" height="12" viewBox="0 0 24 24"><path fill="var(--navy)" d="M6.6 10.8a15 15 0 0 0 6.6 6.6l2.2-2.2a1 1 0 0 1 1-.25 11.4 11.4 0 0 0 3.6.6 1 1 0 0 1 1 1V20a1 1 0 0 1-1 1A17 17 0 0 1 3 4a1 1 0 0 1 1-1h3.5a1 1 0 0 1 1 1c0 1.25.2 2.45.6 3.6a1 1 0 0 1-.25 1z"/></svg>
      <span>11 4000-1234<br>11 4000-5678</span>
    </div>
    <div class="contact contact-address">
      <svg width="11" height="14" viewBox="0 0 24 30"><path fill="var(--navy)" d="M12 0a10 10 0 0 0-10 10c0 7.5 10 20 10 20s10-12.5 10-20A10 10 0 0 0 12 0zm0 14a4 4 0 1 1 0-8 4 4 0 0 1 0 8z"/></svg>
      <span>Av. das Palmeiras, 250 –<br>sala 12, Centro – Campinas SP</span>
    </div>
  </footer>

  <div class="front-brand">
    <span class="brand-name">Alvora</span>
    <span class="tagline">Assessoria e Regularização</span>
  </div>
  <div class="front-rule"></div>
</body>
</html>
```